New Business Card Design Project

Hi there

Could you please make a design that is soft and appealing to people who would purchase gemstones, buy healing jewellery, seek counselling, may seek energy healing and/or learn English. Essentially I'm looking for something with a soft human design. Please incorporate the logo and select font that can be easily read and softer images in the background - but not too busy. I would like it double sided as well.

Optional: Elements could include gemstones, feathers, plants and images that are happy and calming.

Target Market(s)

People into alternative health, those from non-English speaking backgrounds, businesses

Contact Information for Business Card

Leo Marsdon
Mobile: 0412 586 239, Facebook and Instagram Logos,
ABN: 51 742 118 603 (Australian Business Number - small at the bottom)

Requirements
Must have
• My project must have:
- Tranquil Harbor logo
- Symbols that represent the 4 main services: 1. Gemstones/jewellery, 2. counselling, 3. meditation/energy healing, 4. education
Nice to have
• Clear and easy to read.

```html
<!DOCTYPE html>
<html lang="en">
<head>
<meta charset="utf-8">
<title>Tranquil Harbor – Business Card</title>
<link rel="stylesheet" href="https://fonts.googleapis.com/css2?family=Work+Sans:wght@400;500;600&family=Marcellus&display=swap">
<style>
  :root {
    --stage: #1c1c1c;
    --card-dark: #232323;
    --card-dark-2: #333333;
    --card-light: #ffffff;
    --green: #6aa814;
    --teal: #2ab5a8;
    --ink: #2b2b2b;
    --text-light: #f2f2f2;
  }
  * { box-sizing: border-box; margin: 0; padding: 0; }
  html, body { width: 1200px; height: 900px; overflow: hidden; }
  body {
    background: var(--stage);
    font-family: "Work Sans", Arial, sans-serif;
    display: flex;
    flex-direction: column;
    align-items: center;
    justify-content: center;
    gap: 40px;
  }
  .card {
    position: relative;
    width: 660px;
    height: 384px;
    overflow: hidden;
  }

  /* Front */
  .card-front { background: var(--card-dark); }
  .front-texture {
    position: absolute; inset: 0;
    background: radial-gradient(circle at 50% 40%, var(--card-dark-2), var(--card-dark) 75%);
  }
  .front-content {
    position: relative;
    height: 100%;
    display: flex;
    flex-direction: column;
    align-items: center;
    justify-content: center;
    gap: 44px;
    padding-top: 20px;
  }
  .brand-name {
    font-family: "Marcellus", Georgia, serif;
    font-weight: 400;
    color: var(--green);
    text-transform: uppercase;
    letter-spacing: 1px;
  }
  .card-front .brand-name { font-size: 54px; }
  .service-list {
    color: var(--text-light);
    font-size: 17px;
    letter-spacing: 0.8px;
    text-align: center;
    line-height: 1.45;
  }
  .service-list .sep { color: var(--green); padding: 0 4px; }

  /* Back */
  .card-back { background: var(--card-light); }
  .back-logo {
    position: absolute;
    left: 40px; top: 90px;
    width: 260px;
    display: flex;
    flex-direction: column;
    align-items: center;
    gap: 16px;
  }
  .logo-circle {
    width: 62px; height: 62px;
    border-radius: 50%;
    border: 2px solid var(--teal);
  }
  .card-back .brand-name { font-size: 32px; text-align: center; }
  .divider {
    position: absolute;
    left: 330px; top: 88px;
    width: 2px; height: 160px;
    background: var(--green);
  }
  .contact-block {
    position: absolute;
    left: 362px; top: 96px;
  }
  .person-name {
    font-weight: 600;
    font-size: 28px;
    letter-spacing: 1.5px;
    color: var(--green);
    text-transform: uppercase;
  }
  .person-role {
    font-size: 18px;
    color: var(--ink);
    letter-spacing: 1px;
    margin-bottom: 26px;
  }
  .contact-list { list-style: none; }
  .contact-item {
    display: flex; align-items: center; gap: 8px;
    font-size: 19px;
    color: var(--ink);
    letter-spacing: 0.6px;
    line-height: 1.3;
  }
  .contact-icon { width: 13px; height: 13px; flex: none; }
  .bottom-band {
    position: absolute; left: 0; right: 0; bottom: 0;
    height: 12px;
    background: var(--teal);
  }
  .abn-tab {
    position: absolute;
    left: 324px; bottom: 0;
    width: 244px; height: 60px;
    background: var(--green);
    color: #ffffff;
    font-size: 19px;
    letter-spacing: 1.2px;
    display: flex; align-items: center; justify-content: center;
  }
</style>
</head>
<body>
  <section class="card card-front">
    <div class="front-texture" role="img" aria-label="Subtle embossed repeating pattern of overlapping circles on dark card stock"></div>
    <div class="front-content">
      <h1 class="brand-name">Tranquil Harbor</h1>
      <p class="service-list">
        1. Gemstones/jewellery, <span class="sep">|</span> 2. counselling,<br>
        3. meditation/energy healing, <span class="sep">|</span> 4. education
      </p>
    </div>
  </section>

  <section class="card card-back">
    <div class="back-logo">
      <div class="logo-circle"></div>
      <h2 class="brand-name">Tranquil Harbor</h2>
    </div>
    <div class="divider"></div>
    <div class="contact-block">
      <p class="person-name">Leo Marsdon</p>
      <p class="person-role">Founder</p>
      <ul class="contact-list">
        <li class="contact-item">
          <svg class="contact-icon" viewBox="0 0 16 16"><path d="M4 1 L6.5 4.5 L5 6 C6 8 8 10 10 11 L11.5 9.5 L15 12 L13 15 C7 14.5 1.5 9 1 3 Z" fill="var(--green)"/></svg>
          0412 586 239
        </li>
        <li class="contact-item">
          <svg class="contact-icon" viewBox="0 0 16 16"><rect x="1" y="3" width="14" height="10" fill="none" stroke="var(--green)" stroke-width="1.6"/><path d="M1 3 L8 9 L15 3" fill="none" stroke="var(--green)" stroke-width="1.6"/></svg>
          info@tranquilharbor.com
        </li>
        <li class="contact-item">
          <svg class="contact-icon" viewBox="0 0 16 16"><circle cx="8" cy="8" r="6.5" fill="none" stroke="var(--green)" stroke-width="1.4"/><ellipse cx="8" cy="8" rx="3" ry="6.5" fill="none" stroke="var(--green)" stroke-width="1.2"/><path d="M1.5 8 H14.5" stroke="var(--green)" stroke-width="1.2"/></svg>
          www.tranquilharbor.com
        </li>
      </ul>
    </div>
    <div class="bottom-band"></div>
    <div class="abn-tab">ABN: 51 742 118 603</div>
  </section>
</body>
</html>
```